We sell companies excess stock for them

We need a business card for a company based in New Zealand called 'StockHarbor'.

Check out our website to get an idea www.stockharbor.example

We help other businesses to;
- Sell Excess Stock
- Manage Product Returns
- Sell Company Assets

Our logo is attached for your reference
The font used is 'RifficFree-Bold'

Target Market(s)

Businesses

Industry/Entity Type

Business

Contact Information for Business Card

Name: Mark Pellow
Phone: 027 846 2093
email: markpellow@stockharbor.example
website: www.stockharbor.example

Font styles to use
Other font styles liked:
• Unsure

Colors
9bcb3b

Requirements
Must have
• coming soon
Nice to have
• coming soon
Should not have
• coming soon

```html
<!DOCTYPE html>
<html lang="en">
<head>
<meta charset="utf-8">
<title>StockHarbor Business Card</title>
<link rel="stylesheet" href="https://fonts.googleapis.com/css2?family=Lato:wght@300;400;700;900&display=swap">
<style>
  :root {
    --page: #eef0f1;
    --card: #fbfbfb;
    --ink: #2b2b2b;
    --ink-soft: #6f7275;
    --ink-muted: #9a9c9e;
    --band: #f0f0f0;
    --band-strong: #e3e3e3;
    --rule: #d6d6d6;
    --brand-green: #9bcb3b;
    --mascot-orange: #f0a23c;
  }
  * { box-sizing: border-box; margin: 0; padding: 0; }
  html, body {
    width: 1200px;
    height: 800px;
    overflow: hidden;
    background: var(--page);
    font-family: "Lato", Arial, sans-serif;
  }
  .sheet {
    position: relative;
    width: 1200px;
    height: 800px;
    display: flex;
    align-items: center;
    justify-content: center;
    gap: 40px;
  }
  .card {
    position: relative;
    width: 540px;
    height: 328px;
    background: var(--card);
    box-shadow: 0 2px 10px rgba(0,0,0,0.08);
    overflow: hidden;
  }

  /* Front */
  .card--front {
    display: flex;
    align-items: center;
    justify-content: center;
  }
  .wordmark {
    font-weight: 900;
    font-size: 52px;
    letter-spacing: -1px;
    color: var(--ink);
  }

  /* Back */
  .mascot {
    position: absolute;
    top: 22px;
    right: 30px;
    width: 128px;
    height: 124px;
    border-radius: 14px;
    background: linear-gradient(150deg, var(--brand-green) 0%, var(--mascot-orange) 100%);
    opacity: 0.85;
  }
  .name-band {
    position: absolute;
    left: 0;
    top: 196px;
    width: 350px;
    height: 70px;
    background: var(--band);
  }
  .name-block {
    position: absolute;
    right: 12px;
    top: -18px;
    width: 150px;
    height: 56px;
    background: var(--band-strong);
    text-align: right;
    padding: 10px 10px 0 0;
  }
  .name {
    font-size: 18px;
    letter-spacing: 0.5px;
    color: var(--ink);
    text-transform: uppercase;
    white-space: nowrap;
  }
  .name .first { font-weight: 700; }
  .name .last { font-weight: 300; }
  .role {
    margin-top: 3px;
    font-size: 9.5px;
    font-weight: 400;
    letter-spacing: 0.6px;
    color: var(--ink-muted);
    text-transform: uppercase;
  }
  .divider {
    position: absolute;
    left: 350px;
    top: 150px;
    width: 1px;
    height: 120px;
    background: var(--rule);
  }
  .contacts {
    position: absolute;
    left: 362px;
    top: 160px;
    list-style: none;
  }
  .contacts li {
    display: flex;
    align-items: center;
    gap: 6px;
    font-size: 10px;
    line-height: 16px;
    color: var(--ink-soft);
    white-space: nowrap;
  }
  .contacts svg {
    width: 9px;
    height: 9px;
    flex: none;
    fill: var(--ink-soft);
  }
  .contacts .phone { font-size: 12px; }
</style>
</head>
<body>
<main class="sheet">
  <section class="card card--front" aria-label="Card front">
    <h1 class="wordmark">StockHarbor</h1>
  </section>

  <section class="card card--back" aria-label="Card back">
    <div class="mascot" role="img" aria-label="Cartoon delivery mascot in green cap carrying an orange box, giving a thumbs up"></div>

    <div class="name-band">
      <div class="name-block">
        <p class="name"><span class="first">Mark</span> <span class="last">Pellow</span></p>
        <p class="role">Owner &amp; Founder</p>
      </div>
    </div>

    <div class="divider"></div>

    <ul class="contacts">
      <li class="phone">
        <svg viewBox="0 0 10 10" aria-hidden="true"><path d="M2 0.5 L3.6 0.5 L4.2 2.8 L3 3.6 Q4 5.8 6.4 7 L7.2 5.8 L9.5 6.4 L9.5 8 Q9.5 9.5 8 9.5 Q0.5 9 0.5 2 Q0.5 0.5 2 0.5Z"/></svg>
        027 846 2093
      </li>
      <li>
        <svg viewBox="0 0 10 10" aria-hidden="true"><path d="M0.5 2 H9.5 V8.5 H0.5Z M1.2 2.6 L5 5.6 L8.8 2.6" fill="none" stroke="currentColor" stroke-width="1" style="stroke:#6f7275"/></svg>
        markpellow@stockharbor.example
      </li>
      <li>
        <svg viewBox="0 0 10 10" aria-hidden="true"><g fill="none" stroke="#6f7275" stroke-width="0.9"><circle cx="5" cy="5" r="4.3"/><ellipse cx="5" cy="5" rx="1.9" ry="4.3"/><path d="M0.7 5 H9.3"/></g></svg>
        www.stockharbor.example
      </li>
    </ul>
  </section>
</main>
</body>
</html>
```